Brochure Design - Marketing Document - real estate development

It is a 7 Page Proposal document. Please see attached example. It will be used as a marketing proposal document given to potential clients. It is a 'capability statement' used to demonstrate the capability and expertise of the business. I will provide all images and copy to be used in the document. I just need someone to create the template. Use the attached document as a guide for design, style, look and feel

Company name: Tarnwick Communities

I'll be happy to receive the document 80% complete so I can fill in the copy and minor details. All I need from a designer is to format and design a template that I can fill in

Thank you!

Target Market(s)

Corporate investors/clients

Font styles to use
Serif
Sans Serif

Requirements
Must have
• Please use the images of elderly people I have uploaded. There doesn't need to be a photo on every page, but please incorporate the images as you see fit. Also please use the logo attached 'Tarnwick Communities'
• Please see below the template layout/order page by page
• 1st page
• • Branding, photo of beach, headline saying capability statement
• 2nd page
• ABOUT US
• • High level overview from market/retail perspective of what Tarnwick offers and who we are
• • Talk about product and company philosophy
• 3rd page
• OUR TEAM
• • Photos, names and roles
• • Speak generally about immense team experience as a composite body of achievement
• 4th Page
• • List of projects and project values
• Page 5
• • More projects and project values
• Page 6
• • What we are offering our JV partners
• • Benefits and options of model
• Page 7
• • How Tarwick will change the market for the better/ difference between us and old models
• Final page
• • Branding, Address, company details. ABN/CAN
Should not have
• Please do NOT use bright/electric colours of blue, green or orange.
• Please use the attached document as a guide for style, colours and layout

```html
<!DOCTYPE html>
<html lang="en">
<head>
<meta charset="utf-8">
<title>Tarnwick Communities – JV Partners</title>
<link href="https://fonts.googleapis.com/css2?family=Source+Serif+4:wght@400&family=Raleway:wght@400&family=Oswald:wght@600&family=Lato:wght@300&display=swap" rel="stylesheet">
<style>
  :root {
    --paper: #ffffff;
    --ink: #111111;
    --body-ink: #3a3a3a;
    --muted: #8a8a8a;
    --blush: #f0dfd9;
    --bar: #000000;
    --heading-ink: #4a4a4a;
    --photo-pool: #7fb3cf;
    --photo-beach: #b9d2df;
  }
  * { margin: 0; padding: 0; box-sizing: border-box; }
  html, body { width: 1200px; height: 848px; overflow: hidden; background: var(--paper); }
  .spread { position: relative; width: 1200px; height: 848px; background: var(--paper); }

  .edge-bar { position: absolute; top: 212px; height: 424px; width: 36px; background: var(--bar); }
  .edge-bar--left { left: 0; }
  .edge-bar--right { right: 0; }

  .feature-panel { position: absolute; left: 558px; top: 40px; width: 606px; height: 596px; background: var(--blush); }

  .company-label {
    position: absolute; left: 276px; top: 42px;
    font: 400 9.5px/1 "Raleway", sans-serif; letter-spacing: 1.2px;
    color: var(--muted); text-transform: uppercase;
  }

  .page-title {
    position: absolute; left: 120px; top: 98px;
    font: 400 49px/60px "Source Serif 4", serif; color: var(--ink);
  }

  .subhead {
    font: 600 11px/1 "Oswald", sans-serif; letter-spacing: 1.6px;
    text-transform: uppercase; color: var(--ink); margin-bottom: 12px;
  }
  .body-copy { font: 400 11.2px/20.4px "Raleway", sans-serif; color: var(--body-ink); }
  .body-copy + .body-copy { margin-top: 20px; }

  .intro-block { position: absolute; left: 290px; top: 317px; width: 252px; }

  .section-heading {
    position: absolute; left: 768px; top: 66px;
    font: 300 18.5px/33px "Lato", sans-serif; letter-spacing: 1.6px;
    text-transform: uppercase; color: var(--heading-ink);
  }

  .photo { position: absolute; }
  .photo--pool { left: 125px; top: 452px; width: 475px; height: 317px; background: var(--photo-pool); }
  .photo--beach { left: 768px; top: 212px; width: 396px; height: 264px; background: var(--photo-beach); }

  .detail-block { position: absolute; left: 768px; top: 528px; width: 304px; }
</style>
</head>
<body>
<main class="spread">
  <div class="edge-bar edge-bar--left"></div>
  <div class="edge-bar edge-bar--right"></div>
  <div class="feature-panel"></div>

  <p class="company-label">Your Company</p>

  <h1 class="page-title">What we are<br>offering our<br>JV partners</h1>

  <section class="intro-block">
    <h2 class="subhead">Subhead</h2>
    <p class="body-copy">Fusce sollicitudin ut risus id maximus. Etiam porttitor eget velit non laoreet. Nunc sed odio sem. Vestibulum ante ipsum primis in faucibus orci luctus et ultrices posuere cubilia Curae; Nullam et bibendum est.</p>
  </section>

  <div class="photo photo--pool" role="img" aria-label="Photo of a senior swimmer with a towel beside an indoor pool"></div>

  <h2 class="section-heading">How Tarwick will change<br>the market for the better/<br>difference between us and<br>old models</h2>

  <div class="photo photo--beach" role="img" aria-label="Photo of a group of seniors in sun hats on a sunny beach"></div>

  <section class="detail-block">
    <h3 class="subhead">Subhead</h3>
    <p class="body-copy">Suspendisse potenti. Duis eu tempor dui, vel tristique<br>dolor. Nullam dictum ornare purus, vitae posuere tellus<br>malesuada nec. Duis sit amet eros vitae dolor tempor<br>fermentum ut in purus. Maecenas sit amet facilisis<br>metus, vel varius mi. Aliquam sit amet cursus metus.</p>
    <p class="body-copy">Maecenas eu volutpat nibh, ut condimentum augue.<br>Praesent quis consequat nunc. Ut tempus quam at<br>lectus malesuada volutpat. Cras commodo sodales<br>congue. Phasellus ullamcorper vehicula leo ut mollis.</p>
  </section>
</main>
</body>
</html>
```